Local massage therapist needs some new marketing material

Hi there! I am a massage therapist here in Denver, CO in Brindle Hollow(shopping and art district) of the city. My business is called Lunora Massage of Denver. My practice has an eastern influence and I do reflexology, thai massage and use Chinese herbs, etc. I know all my clients and pay close attention to details. I am also very respectful of tradition and it shows in how I work. I tend to like modern, clean, fun, Asian designs. I am wanting a new business card and brochure. I have a logo and branding for my business that I want used in the design. Currently, the sign for my building is purple and I think my logo was designed to be purple. I will attach pictures of it and can send whatever files are necessary so it can be integrated into the brochure, etc. I like the purple but open to using other colors as well. Thanks!
My website is lunoramassagestudio.example where info can be gathered about me and services/fees for brochure.
Updates

Just increased budget. Please see new feedback in discussion thread.

Thanks!

                                       HEY ALL,

Just wanted to let you know that I made a change to my website. It is on the Prices Page. I no longer have the frequent  flyer prices but I added discounts. Let me know if you have any questions. Thanks so much!

Target Market(s)

healthy, urban, educated, upper middle class, yogis

Industry/Entity Type

Marketing

Requirements
Must have
• logo stays purple
Should not have
• not too busy

```html
<!DOCTYPE html>
<html lang="en">
<head>
<meta charset="utf-8">
<title>Lunora Massage of Denver – Stationery</title>
<link href="https://fonts.googleapis.com/css2?family=Arimo:wght@400;700&display=swap" rel="stylesheet">
<style>
  :root {
    --purple: #74359a;
    --purple-deep: #5e2386;
    --purple-light: #9a62bd;
    --rose: #6a2c96;
    --text-purple: #8a4fb0;
    --paper: #f4f4f4;
    --paper-shade: #e2e2e2;
    --white: #ffffff;
    --backdrop: #ece7ef;
  }
  * { margin: 0; padding: 0; box-sizing: border-box; }
  html, body { width: 1200px; height: 1200px; overflow: hidden; }
  body {
    background: var(--backdrop);
    font-family: 'Arimo', Arial, sans-serif;
    position: relative;
  }

  /* Letterhead */
  .letterhead {
    position: absolute; left: 51px; top: 136px;
    width: 570px; height: 805px;
    background: linear-gradient(180deg, var(--paper) 0%, var(--paper-shade) 100%);
    overflow: hidden;
    box-shadow: 0 6px 18px rgba(60, 20, 80, .18);
  }
  .letterhead-art { position: absolute; inset: 0; width: 100%; height: 100%; }
  .letterhead-body {
    position: absolute; left: 6px; top: 142px; width: 560px;
    color: var(--text-purple); font-size: 22px; line-height: 31.5px;
    word-break: break-all;
  }
  .letterhead-title { font-size: 22px; font-weight: 400; margin-bottom: 24px; }
  .rose-cluster {
    position: absolute; left: 0; bottom: 0; width: 135px; height: 115px;
    border-radius: 0 70px 0 0;
    background: radial-gradient(ellipse at 40% 60%, #8645b4 0%, var(--rose) 50%, #4d1a72 100%);
  }

  /* Business card — back */
  .card-back {
    position: absolute; left: 703px; top: 137px;
    width: 464px; height: 287px;
    background: var(--purple);
    border: 5px solid var(--white);
    box-shadow: 0 6px 18px rgba(60, 20, 80, .2);
    display: flex; flex-direction: column; align-items: center; justify-content: center;
  }
  .brand-mark { display: flex; align-items: center; gap: 14px; }
  .brand-dot { width: 18px; height: 18px; border-radius: 50%; border: 2px solid var(--white); }
  .brand-name { color: var(--white); font-size: 30px; font-weight: 400; letter-spacing: 8px; }

  /* Business card — front */
  .card-front {
    position: absolute; left: 675px; top: 486px;
    width: 464px; height: 287px;
    background: var(--white);
    transform: rotate(-27deg);
    box-shadow: 0 6px 18px rgba(60, 20, 80, .2);
    overflow: hidden;
  }
  .card-front-art { position: absolute; inset: 0; width: 100%; height: 100%; }
  .card-brand {
    position: absolute; right: 18px; top: 150px; text-align: right;
    color: var(--purple);
  }
  .card-brand .brand-name { color: var(--purple); font-size: 26px; letter-spacing: 5px; margin-right: -5px; }
  .card-brand .brand-sub { font-size: 12px; font-weight: 700; letter-spacing: 0.3px; }
  .card-person { position: absolute; left: 22px; top: 92px; color: var(--white); }
  .card-person-name { font-size: 22px; font-weight: 700; }
  .card-person-role { font-size: 12px; font-weight: 700; }
  .card-contact {
    position: absolute; left: 22px; bottom: 22px;
    color: var(--white); font-size: 11px; font-weight: 700; line-height: 17px; list-style: none;
  }
  .card-contact li { display: flex; align-items: center; gap: 6px; }
  .card-contact svg { width: 10px; height: 10px; fill: var(--white); }
</style>
</head>
<body>

<section class="letterhead">
  <svg class="letterhead-art" viewBox="0 0 570 805" preserveAspectRatio="none" aria-hidden="true">
    <defs>
      <linearGradient id="topBand" x1="0" y1="0" x2="1" y2="0">
        <stop offset="0" stop-color="#9a62bd"/>
        <stop offset="1" stop-color="#74359a"/>
      </linearGradient>
      <linearGradient id="bottomBand" x1="0" y1="0" x2="1" y2="0">
        <stop offset="0" stop-color="#5e2386"/>
        <stop offset="1" stop-color="#9a62bd"/>
      </linearGradient>
    </defs>
    <path d="M0 0 H570 V18 C470 10 420 20 360 45 C290 75 250 85 180 80 C110 76 60 92 0 104 Z" fill="url(#topBand)"/>
    <path d="M0 0 H570 V10 C490 0 430 8 370 30 C300 56 250 62 180 58 C110 55 60 70 0 84 Z" fill="#74359a" opacity=".45"/>
    <path d="M0 805 V770 C140 790 300 785 420 760 C480 748 530 735 570 728 V805 Z" fill="url(#bottomBand)"/>
  </svg>

  <div class="letterhead-body">
    <h1 class="letterhead-title">Welcome</h1>
    <p>&nbsp;Welcome to Lunora Massage of Denver. The office is located in an updated turn of the century house. A harmonious blend of old and new and a blissful escape from the hustle and bustle of the city. My mission is to provide clients with peace, relaxation and well-being of body, mind and spirit through the healing power of massage therapy. Lunora is an ancient Pali word dating back more than 2,500 years to the time of Buddha. It is often translated as "loving-kindness", or unconditional love. At Lunora Massage, I work mindfully to cultivate loving-kindness, forgiveness, joy and serenity.</p>
    <p>&nbsp;Every person is a whole being, not a symptom or disorder, and I believe that it is within every individual's power to lead a life of healing.</p>
  </div>

  <div class="rose-cluster" role="img" aria-label="Cluster of purple roses"></div>
</section>

<section class="card-back">
  <div class="brand-mark">
    <span class="brand-dot"></span>
    <span class="brand-name">LUNORA</span>
  </div>
</section>

<section class="card-front">
  <svg class="card-front-art" viewBox="0 0 464 287" preserveAspectRatio="none" aria-hidden="true">
    <path d="M0 0 H165 C180 110 215 210 290 287 H0 Z" fill="#74359a"/>
    <path d="M165 0 H182 C198 110 232 205 308 287 H290 C215 210 180 110 165 0 Z" fill="#ffffff"/>
    <path d="M182 0 H204 C218 105 250 200 328 287 H308 C232 205 198 110 182 0 Z" fill="#9a62bd"/>
  </svg>

  <div class="card-brand">
    <div class="brand-name">LUNORA</div>
    <div class="brand-sub">MASSAGE OF DENVER</div>
  </div>

  <div class="card-person">
    <div class="card-person-name">Your name</div>
    <div class="card-person-role">Your Designation</div>
  </div>

  <ul class="card-contact">
    <li><svg viewBox="0 0 10 10"><path d="M5 0 C2.5 0 1 2 1 4 C1 6.5 5 10 5 10 C5 10 9 6.5 9 4 C9 2 7.5 0 5 0 Z"/></svg>1480 Wren St, Denver, CO 80206</li>
    <li><svg viewBox="0 0 10 10"><rect x="2" y="0" width="6" height="10" rx="1"/></svg>555.013.0187</li>
    <li><svg viewBox="0 0 10 10"><path d="M0 2 H10 V8 H0 Z"/></svg>info@lunoramassagestudio.example</li>
    <li><svg viewBox="0 0 10 10"><path d="M2 1 L4 1 L5 3 L4 4 C4.5 5.5 5.5 6 6 6 L7 5 L9 6 L9 8 C5 9 1 5 2 1 Z"/></svg>555.013.0187</li>
    <li><svg viewBox="0 0 10 10"><circle cx="5" cy="5" r="4.5"/></svg>www.lunoramassagestudio.example</li>
  </ul>
</section>

</body>
</html>
```